Zielgruppe
Was machen wir: Datenschutz und Informationssicherheit als Dienstleistung.
Zielgruppe: Mittelständische Unternehmenskunden 500 -5000 Mitarbeiter
Aufgabenstellung
Wir benötigen eine neue Powerpoint Vorlage. Die alte Vorlage ist nicht mehr zeitgemäß.
Format: DIN 16:9
Standardschriftart: Calibri
Zielgruppe: Mittleres und gehobenes Management
CI: Unsere Farben können auf unserer Webseite eingesehen werden.

```html
<!DOCTYPE html>
<html lang="de">
<head>
<meta charset="utf-8">
<title>Danke für Ihre Aufmerksamkeit</title>
<link href="https://fonts.googleapis.com/css2?family=Carlito:wght@400;700&display=swap" rel="stylesheet">
<style>
  :root {
    --brand-orange: #ff8000;
    --slide-blue: #3f5089;
    --slide-blue-light: #4a5d9a;
    --slide-blue-dark: #394a82;
    --text-white: #ffffff;
    --brand-grey: #8f9bbf;
  }
  html, body {
    margin: 0;
    padding: 0;
    width: 1200px;
    height: 675px;
    overflow: hidden;
    background: var(--slide-blue);
  }
  .slide {
    position: relative;
    width: 1200px;
    height: 675px;
    overflow: hidden;
    font-family: "Carlito", "Calibri", sans-serif;
  }
  .slide-backdrop {
    position: absolute;
    inset: 0;
    background:
      linear-gradient(172deg, rgba(255,255,255,0.06) 0%, rgba(255,255,255,0) 40%),
      linear-gradient(180deg, var(--slide-blue-light) 0%, var(--slide-blue) 45%, var(--slide-blue-dark) 100%);
  }
  .edge-bar {
    position: absolute;
    top: 0;
    width: 12px;
    height: 675px;
    background: var(--brand-orange);
  }
  .edge-bar--left { left: 0; }
  .edge-bar--right { right: 0; }
  .closing-art {
    position: absolute;
    inset: 0;
  }
  .headline { font-weight: 700; fill: var(--brand-orange); font-size: 92px; }
  .message { font-weight: 400; fill: var(--text-white); font-size: 97px; letter-spacing: 0.5px; }
  .farewell { font-weight: 400; fill: var(--brand-orange); font-size: 55px; letter-spacing: 0.5px; }
  .company-name {
    position: absolute;
    right: 34px;
    bottom: 26px;
    font-family: "Carlito", "Calibri", sans-serif;
    font-weight: 700;
    font-size: 14px;
    color: var(--brand-grey);
    letter-spacing: 0.3px;
  }
</style>
</head>
<body>
  <main class="slide">
    <div class="slide-backdrop" role="img" aria-label="Unscharfes Hintergrundfoto mit blauen Lichtstreifen"></div>
    <div class="edge-bar edge-bar--left"></div>
    <div class="edge-bar edge-bar--right"></div>

    <svg class="closing-art" width="1200" height="675" viewBox="0 0 1200 675">
      <circle cx="561" cy="337" r="311" fill="none" stroke="var(--brand-orange)" stroke-width="2.5"/>
      <text class="headline" x="561" y="175" text-anchor="middle">DANKE</text>
      <text class="message" x="561" y="269" text-anchor="middle">für Ihre</text>
      <text class="message" x="561" y="362" text-anchor="middle">Aufmerk-</text>
      <text class="message" x="561" y="456" text-anchor="middle">samkeit!</text>
      <line x1="353" y1="491" x2="769" y2="491" stroke="var(--text-white)" stroke-width="2.5"/>
      <text class="farewell" x="561" y="553" text-anchor="middle">Auf Wiedersehen</text>
    </svg>

    <div class="company-name">Nordwall Beratung</div>
  </main>
</body>
</html>
```